Präsentationsvorlagen/Workbook für Coaching - Yoga - Training
Zielgruppe
Coaching - Yoga - Training, d.h. Yogaunterricht, Einzelcoaching, Seminare und Workshops rund um das Thema Stress/Resilienz/Achtsamkeit
Zielgruppe sind einerseits überwiegend Frauen, aber auch Firmenkunden, die für ihre Mitarbeiter Seminare und Yoga anbieten.
Aufgabenstellung
Ich benötige einen professionellen ppt Auftritt für Präsentationen/Workbooks mit meinen Firmenfarben (grau, weiß, rosa, beige) in den mein Logo integriert ist.
Das Design sollte dem Thema entsprechend 'warm' sein aber die nötige Professionalität für Firmenkunden ausstrahlen.

```html
<!DOCTYPE html>
<html lang="de">
<head>
<meta charset="utf-8">
<title>Lena Marwitz – Präsentationsvorlagen</title>
<link rel="stylesheet" href="https://fonts.googleapis.com/css2?family=Cinzel:wght@400;600;700&family=Open+Sans:wght@400;600&display=swap">
<style>
  :root{
    --stage:#e9e6e6;
    --cream:#f3eee7;
    --ivory:#f7f4f0;
    --beige:#d8ab8a;
    --beige-dark:#cf9f7c;
    --rose:#b2417c;
    --graphite:#3d3839;
    --white:#ffffff;
  }
  *{margin:0;padding:0;box-sizing:border-box}
  html,body{width:1200px;height:622px;overflow:hidden;background:var(--stage)}
  .canvas{position:relative;width:1200px;height:622px}
  .slide{position:absolute;width:368px;height:207px;overflow:hidden;box-shadow:0 6px 18px rgba(60,50,50,.14)}
  .slide svg.shapes{position:absolute;inset:0;width:100%;height:100%}
  .slide--training{left:28px;top:94px;background:var(--cream)}
  .slide--hero{left:416px;top:94px}
  .slide--yoga{left:804px;top:94px;background:var(--ivory)}
  .slide--coaching{left:222px;top:321px;background:var(--beige)}
  .slide--cover{left:610px;top:321px;background:var(--ivory)}

  .title{position:absolute;font-family:"Cinzel",serif;font-weight:700;font-size:15px;letter-spacing:.5px;text-transform:uppercase}
  .subtitle{position:absolute;font-family:"Cinzel",serif;font-weight:400;font-size:7.5px;line-height:1.15;letter-spacing:.3px}
  .body{position:absolute;font-family:"Open Sans",sans-serif;font-size:5px;line-height:1.45}

  .slide--training .title,.slide--training .subtitle,.slide--training .body{color:var(--rose)}
  .slide--coaching .title,.slide--coaching .subtitle,.slide--coaching .body,
  .slide--yoga .title,.slide--yoga .subtitle,.slide--yoga .body{color:var(--white)}

  .brand-mark{position:absolute;top:12px;right:12px;display:flex;align-items:center;gap:3px;font-family:"Cinzel",serif;font-size:5.5px;font-weight:600}
  .brand-mark i{display:block;width:9px;height:9px;border:1px solid currentColor;border-radius:50%}
  .slide--training .brand-mark,.slide--cover .brand-mark{color:var(--rose)}
  .slide--yoga .brand-mark{color:var(--white)}

  .cover-brand{position:absolute;left:0;right:0;top:72px;text-align:center}
  .cover-brand .dot{display:block;margin:0 auto 8px;width:26px;height:26px;border:2px solid var(--rose);border-radius:50%}
  .cover-brand .name{font-family:"Cinzel",serif;font-size:21px;font-weight:400;color:var(--graphite);letter-spacing:.6px}
  .cover-brand .tagline{font-family:"Cinzel",serif;font-size:7.5px;color:var(--rose);letter-spacing:.5px;margin-top:1px}
</style>
</head>
<body>
<main class="canvas">

  <!-- Training -->
  <section class="slide slide--training">
    <svg class="shapes" viewBox="0 0 368 207" aria-hidden="false">
      <defs>
        <linearGradient id="lakeSunrise" x1="0" y1="0" x2="0" y2="1">
          <stop offset="0" stop-color="#e9c0a6"/>
          <stop offset=".45" stop-color="#d07a52"/>
          <stop offset=".7" stop-color="#8a5a4c"/>
          <stop offset="1" stop-color="#2e2a2c"/>
        </linearGradient>
      </defs>
      <path d="M300 207 C300 170 330 140 368 132 L368 207 Z" fill="#ffffff" opacity=".8"/>
      <circle cx="254" cy="62" r="52" fill="url(#lakeSunrise)" role="img" aria-label="Foto: Sonnenaufgang über einem nebligen See mit Ruderboot"/>
    </svg>
    <div class="brand-mark"><i></i>Lena Marwitz</div>
    <h2 class="title" style="left:34px;top:38px">Training</h2>
    <p class="subtitle" style="left:34px;top:58px">_ Mit Freude Neues erlernen!</p>
    <p class="body" style="left:30px;top:80px;width:150px">Als zertifizierte Trainerin begleite ich Menschen dabei, sich weiterzuentwickeln. In praxisnahen Seminaren verbinde ich Fachwissen mit Freude am Lernen – individuell auf Ihr Team abgestimmt. Sprechen Sie mich gerne an!</p>
  </section>

  <!-- Bildfolie -->
  <section class="slide slide--hero">
    <svg class="shapes" viewBox="0 0 368 207">
      <defs>
        <linearGradient id="heroGlow" x1="0" y1="0" x2="0" y2="1">
          <stop offset="0" stop-color="#f1d9cc"/>
          <stop offset=".55" stop-color="#f4e2d4"/>
          <stop offset="1" stop-color="#dcbba8"/>
        </linearGradient>
      </defs>
      <rect width="368" height="207" fill="url(#heroGlow)" role="img" aria-label="Foto: Frau in Yoga-Pose bei Sonnenaufgang am Meer, in zartem Pfirsichton überblendet"/>
    </svg>
  </section>

  <!-- Yoga -->
  <section class="slide slide--yoga">
    <svg class="shapes" viewBox="0 0 368 207">
      <defs>
        <linearGradient id="duskSky" x1="0" y1="0" x2="0" y2="1">
          <stop offset="0" stop-color="#c9b4d6"/>
          <stop offset=".55" stop-color="#ead7df"/>
          <stop offset=".72" stop-color="#6b5a5e"/>
          <stop offset="1" stop-color="#1e1b1d"/>
        </linearGradient>
      </defs>
      <path d="M132 0 L368 0 L368 207 L0 207 L0 170 C60 160 110 150 125 110 C140 70 120 30 132 0 Z" fill="var(--beige)"/>
      <circle cx="64" cy="62" r="50" fill="url(#duskSky)" role="img" aria-label="Foto: Silhouette einer Person in Yoga-Standhaltung vor Abendhimmel"/>
    </svg>
    <div class="brand-mark"><i></i>Lena Marwitz</div>
    <h2 class="title" style="left:150px;top:46px">Yoga</h2>
    <p class="subtitle" style="left:150px;top:65px;width:180px">_ Innere Ruhe und Steigerung<br>des Wohlbefindens</p>
    <p class="body" style="left:150px;top:92px;width:185px">„Yoga ist das Zur-Ruhe-Kommen der Gedanken im Geist.“ Ich unterrichte sanftes Hatha Yoga mit Atemübungen, Meditation und Tiefenentspannung – für Einsteiger und Geübte.</p>
  </section>

  <!-- Coaching -->
  <section class="slide slide--coaching">
    <svg class="shapes" viewBox="0 0 368 207">
      <defs>
        <linearGradient id="eveningLake" x1="0" y1="0" x2="0" y2="1">
          <stop offset="0" stop-color="#5d5f9c"/>
          <stop offset=".4" stop-color="#d9a4b4"/>
          <stop offset=".5" stop-color="#7a5a82"/>
          <stop offset="1" stop-color="#1c1a35"/>
        </linearGradient>
      </defs>
      <path d="M0 0 L52 0 C38 40 60 80 54 120 C48 160 62 185 60 207 L0 207 Z" fill="url(#eveningLake)" role="img" aria-label="Foto: ruhiger See in der Abenddämmerung mit Bergsilhouette"/>
    </svg>
    <h2 class="title" style="left:95px;top:42px">Coaching</h2>
    <p class="subtitle" style="left:95px;top:62px;width:200px">_ Zurück zur Selbstfürsorge<br>&nbsp;&nbsp;und Selbstbestimmtheit</p>
    <p class="body" style="left:93px;top:94px;width:190px">Wo stehst Du heute? Und wo möchtest Du hin?<br>Coaching ist ein lösungsorientierter Prozess, der Dich in herausfordernden Lebenssituationen begleitet. Gemeinsam schaffen wir Klarheit für Dein Ziel und aktivieren Deine Ressourcen.</p>
  </section>

  <!-- Titelfolie -->
  <section class="slide slide--cover">
    <svg class="shapes" viewBox="0 0 368 207">
      <path d="M0 0 L130 0 C90 12 40 18 0 30 Z" fill="var(--beige)" opacity=".55"/>
      <path d="M0 190 C90 165 200 150 280 162 C320 168 345 168 368 162 L368 207 L0 207 Z" fill="var(--beige)"/>
    </svg>
    <div class="brand-mark"><i></i></div>
    <div class="cover-brand">
      <span class="dot"></span>
      <p class="name">Lena Marwitz</p>
      <p class="tagline">Coaching - Yoga - Training</p>
    </div>
  </section>

</main>
</body>
</html>
```